Wall Design - Moden Construction Graphic Needed

Looking to create a modern graphic that will accent our signature wall for our space. I would like to incorporate our logo into design that includes construction elements or backgrounds such as "blueprints" or similar. I am also a fan of inspiration, team building, customer service, types of saying. Ideally the wall would be modern, incorporating our logo, construction and motivational blend...

Industry/Entity Type

Construction

Font styles to use
Sans Serif

Colors
faa54b
f78f20
edf6f7

Requirements
Must have
• Logo
Construction Elements
Motivational Elements
Nice to have
• Blueprint Feel

```html
<!DOCTYPE html>
<html lang="en">
<head>
<meta charset="utf-8">
<title>Harlow Construction – Signature Wall</title>
<link rel="stylesheet" href="https://fonts.googleapis.com/css2?family=Archivo+Black&family=Didact+Gothic&display=swap">
<style>
  :root {
    --paper: #ffffff;
    --green: #98d300;
    --orange: #ff6600;
    --gold: #f2c60e;
    --blue: #007396;
    --chevron: #fbe800;
    --ink: #ffffff;
  }
  html, body { margin: 0; padding: 0; overflow: hidden; background: var(--paper); }
  .wall {
    position: relative;
    width: 1045px;
    height: 1200px;
    overflow: hidden;
    background: var(--paper);
    font-family: "Didact Gothic", sans-serif;
    color: var(--ink);
  }
  .panel { position: absolute; width: 442px; height: 511px; }
  .panel--inspiration { left: 52px; top: 73px; background: var(--green); }
  .panel--team { left: 528px; top: 73px; background: var(--orange); }
  .panel--service { left: 52px; top: 607px; background: var(--gold); }
  .panel--blueprint { left: 528px; top: 607px; background: var(--blue); }

  .chevrons { position: absolute; left: 0; top: 0; width: 1045px; height: 1200px; }

  .headline {
    position: absolute;
    margin: 0;
    font-family: "Archivo Black", sans-serif;
    font-weight: 400;
    font-size: 79px;
    line-height: 64px;
    letter-spacing: -2px;
    text-align: right;
  }
  .headline--inspiration { right: calc(1045px - 240px); top: 222px; }
  .headline--team { right: calc(1045px - 922px); top: 229px; }
  .headline--service { right: calc(1045px - 362px); top: 652px; }

  .body-copy {
    position: absolute;
    margin: 0;
    font-size: 16.6px;
    line-height: 19.7px;
  }
  .body-copy--inspiration { left: 250px; top: 144px; }
  .body-copy--team { left: 550px; top: 311px; }
  .body-copy--service { left: 187px; top: 927px; }
  .body-copy--blueprint { left: 743px; top: 694px; }

  .brand {
    position: absolute;
    left: 712px;
    top: 124px;
    display: flex;
    align-items: center;
    gap: 10px;
  }
  .brand__mark { width: 40px; height: 40px; background: var(--ink); }
  .brand__name {
    font-family: "Didact Gothic", sans-serif;
    font-size: 19px;
    line-height: 20px;
    letter-spacing: 1px;
    text-transform: uppercase;
    color: var(--ink);
  }

  .floorplan {
    position: absolute;
    left: 546px;
    top: 836px;
    width: 396px;
    height: 266px;
    background: linear-gradient(135deg, #0a86ab 0%, #006a8c 100%);
    border: 2px solid rgba(255,255,255,0.55);
    box-sizing: border-box;
  }
</style>
</head>
<body>
<main class="wall">
  <div class="panel panel--inspiration"></div>
  <div class="panel panel--team"></div>
  <div class="panel panel--service"></div>
  <div class="panel panel--blueprint"></div>

  <svg class="chevrons" viewBox="0 0 1790 2080" preserveAspectRatio="none" aria-hidden="true">
    <g fill="var(--chevron)">
      <polygon points="674,900 760,900 895,1031 760,1163 674,1163 810,1031"/>
      <polygon points="843,900 929,900 1064,1031 929,1163 843,1163 979,1031"/>
      <polygon points="1004,900 1090,900 1225,1031 1090,1163 1004,1163 1140,1031"/>
      <polygon points="1182,900 1268,900 1403,1031 1268,1163 1182,1163 1318,1031"/>
      <polygon points="1364,900 1450,900 1585,1031 1450,1163 1364,1163 1500,1031"/>
      <polygon points="1530,900 1616,900 1751,1031 1616,1163 1530,1163 1666,1031"/>
    </g>
  </svg>

  <div class="brand">
    <span class="brand__mark"></span>
    <span class="brand__name">Harlow<br>Construction</span>
  </div>

  <h2 class="headline headline--inspiration">INS<br>PIR<br>ATI<br>ON</h2>
  <p class="body-copy body-copy--inspiration">Lorem ipsum dolor sit amet,<br>consectetuer adipiscing elit,<br>sed diam nonummy nibh<br>euismod tincidunt ut laoreet<br>dolore magna aliquam erat<br>volutpat. Ut wisi enim ad<br>minim veniam, quis nostrud<br>exerci tation ullamcorper<br>suscipit lobortis nisl ut aliquip</p>

  <h2 class="headline headline--team">TEAM<br>BUI<br>LDI<br>NG</h2>
  <p class="body-copy body-copy--team">Lorem ipsum dolor sit amet,<br>consectetuer adipiscing elit,<br>sed diam nonummy nibh<br>euismod tincidunt ut laoreet<br>dolore magna aliquam erat<br>volutpat. Ut wisi enim ad<br>minim veniam, quis nostrud<br>exerci tation ullamcorper<br>suscipit lobortis nisl ut aliquip</p>

  <h2 class="headline headline--service">CUST<br>OMER<br>SER<br>VICE</h2>
  <p class="body-copy body-copy--service">Lorem ipsum dolor sit amet, consec-<br>tetuer adipiscing elit, sed diam<br>nonummy nibh euismod tincidunt ut<br>laoreet dolore magna aliquam erat<br>volutpat. Ut wisi enim ad minim<br>veniam, quis nostrud exerci tation<br>ullamcorper suscipit lobortis nisl ut</p>

  <p class="body-copy body-copy--blueprint">Lorem ipsum dolor sit amet,<br>consectetuer adipiscing elit,<br>sed diam nonummy nibh<br>euismod tincidunt ut laoreet<br>dolore magna aliquam erat<br>volutpat. Ut wisi enim ad</p>

  <div class="floorplan" role="img" aria-label="White line blueprint floor plan of an apartment with dimension arrows"></div>
</main>
</body>
</html>
```